A online shop for solid wood need a Stationary design

A new online shop (in Austria and Germany) for solid wood and steel furniture (feldmark-tischwerk) needs a Stationay design (letterhead, business card, envelope etc...). Dining tables, coffee tables, TV furniture and similar furniture will be sold. Everything will be custom made.

```html
<!DOCTYPE html>
<html lang="en">
<head>
<meta charset="utf-8">
<title>Feldmark Tischwerk – Business Card</title>
<link rel="stylesheet" href="https://fonts.googleapis.com/css2?family=Lato:wght@400;900&family=Oswald:wght@500&display=swap">
<style>
  :root {
    --backdrop: #dedede;
    --card: #262626;
    --red: #e71c24;
    --white: #ffffff;
  }
  * { box-sizing: border-box; margin: 0; padding: 0; }
  html, body { width: 1200px; height: 1200px; overflow: hidden; }
  body {
    background: var(--backdrop);
    position: relative;
    font-family: "Lato", Arial, sans-serif;
  }
  .card {
    position: absolute;
    left: 262px;
    width: 686px;
    height: 392px;
    border-radius: 20px;
    background: var(--card);
    overflow: hidden;
  }
  .card--front { top: 165px; }
  .card--back { top: 653px; }

  /* Front: large brand name in the left field */
  .brand-feature {
    position: absolute;
    left: 44px;
    top: 50%;
    transform: translateY(-50%);
    width: 360px;
  }
  .brand-feature__square {
    display: block;
    width: 84px;
    height: 84px;
    background: var(--red);
    border-radius: 6px;
    margin-bottom: 26px;
  }
  .brand-feature__name {
    font-weight: 900;
    font-size: 54px;
    line-height: 58px;
    letter-spacing: 1px;
    color: var(--red);
    text-transform: uppercase;
  }

  .contact {
    position: absolute;
    right: 37px;
    top: 162px;
    text-align: right;
    color: var(--white);
    font-size: 15.5px;
    line-height: 19px;
  }
  .contact__name {
    font-family: "Oswald", "Arial Narrow", sans-serif;
    font-weight: 500;
    font-size: 27px;
    line-height: 30px;
    color: var(--red);
    text-transform: uppercase;
  }
  .contact__role { margin-bottom: 17px; }
  .contact__address { margin-bottom: 13px; }
  .contact__line {
    display: flex;
    justify-content: flex-end;
    align-items: center;
    gap: 8px;
  }
  .contact__line svg { width: 13px; height: 13px; flex: none; }

  /* Back: centered brand lockup */
  .lockup {
    position: absolute;
    left: 0; right: 0;
    top: 107px;
    display: flex;
    flex-direction: column;
    align-items: center;
  }
  .lockup__square {
    width: 110px;
    height: 110px;
    background: var(--red);
    border-radius: 6px;
    margin-bottom: 24px;
  }
  .lockup__name {
    font-weight: 900;
    color: var(--red);
    text-transform: uppercase;
    text-align: center;
  }
  .lockup__primary {
    display: block;
    font-size: 46px;
    line-height: 50px;
    letter-spacing: 3px;
  }
  .lockup__secondary {
    display: block;
    font-size: 15px;
    line-height: 20px;
    letter-spacing: 6px;
    margin-top: 2px;
  }
</style>
</head>
<body>

<section class="card card--front">
  <div class="brand-feature">
    <span class="brand-feature__square"></span>
    <p class="brand-feature__name">Feldmark<br>Tischwerk</p>
  </div>
  <div class="contact">
    <p class="contact__name">Lukas Brenner</p>
    <p class="contact__role">President</p>
    <p class="contact__address">2140 Birchwood Lane<br>Juneau, Alaska 34812</p>
    <p class="contact__line">369-408-7721
      <svg viewBox="0 0 16 16" aria-hidden="true"><path fill="#e71c24" d="M3.6 1.2l2.2 2.6-1.2 1.8c.9 2.2 2.5 3.9 4.7 4.9l1.8-1.2 2.6 2.2-1.3 2.3C7 13.4 2.6 9 1.4 2.5z"/></svg>
    </p>
    <p class="contact__line">369-603-1194
      <svg viewBox="0 0 16 16" aria-hidden="true"><rect x="4" y="1" width="8" height="14" rx="1.5" fill="none" stroke="#e71c24" stroke-width="1.6"/><rect x="7" y="12" width="2" height="1.2" fill="#e71c24"/></svg>
    </p>
    <p class="contact__line">name@feldmarktischwerk.com
      <svg viewBox="0 0 16 16" aria-hidden="true"><rect x="1" y="3.5" width="14" height="9" fill="#e71c24"/><path d="M1.5 4l6.5 5 6.5-5" fill="none" stroke="#262626" stroke-width="1.2"/></svg>
    </p>
    <p class="contact__line">www.feldmarktischwerk.com
      <svg viewBox="0 0 16 16" aria-hidden="true"><circle cx="8" cy="8" r="6.5" fill="#e71c24"/><path d="M1.5 8h13M8 1.5c-2.5 3-2.5 10 0 13M8 1.5c2.5 3 2.5 10 0 13" fill="none" stroke="#262626" stroke-width="1"/></svg>
    </p>
  </div>
</section>

<section class="card card--back">
  <div class="lockup">
    <span class="lockup__square"></span>
    <p class="lockup__name">
      <span class="lockup__primary">Feldmark</span>
      <span class="lockup__secondary">Tischwerk</span>
    </p>
  </div>
</section>

</body>
</html>
```